Business Card Design Project

Basic business card with minimal details. I just need company name, email & web address, telephone and my name.
I would like the back of the card to be grey with my logo & company name centred.

Target Market(s)

Architects
Builders
Property Developers

Industry/Entity Type

Business

Font styles to use
Sans Serif

Colors

Designer to choose colors to be used in the design.

Requirements
Must have
• Framewise Build
Marcus Helby - Director
M: 0427 593184
E: marcus@framewisebuild.com.au
W: www.framewisebuild.com.au
Should not have
• No other images or pictures

```html
<!DOCTYPE html>
<html lang="en">
<head>
<meta charset="utf-8">
<title>Framewise Build – Business Card</title>
<link href="https://fonts.googleapis.com/css2?family=Arimo:wght@400;700&display=swap" rel="stylesheet">
<style>
  :root {
    --page-bg: #e6e6e5;
    --card-grey: #807f7d;
    --card-white: #ffffff;
    --name-grey: #8c8c8c;
    --accent-red: #c8302c;
    --text-light: #ffffff;
  }
  * { margin: 0; padding: 0; box-sizing: border-box; }
  html, body {
    width: 1200px; height: 999px; overflow: hidden;
    background: var(--page-bg);
    font-family: "Arimo", Arial, sans-serif;
  }
  .canvas { position: relative; width: 1200px; height: 999px; }

  .card-front {
    position: absolute; left: 279px; top: 72px; width: 688px; height: 392px;
    background: var(--card-grey);
  }
  .brand {
    position: absolute; left: 20px; top: 0; height: 392px; width: 660px;
    display: flex; align-items: center; gap: 26px; padding-bottom: 50px;
  }
  .brand-square {
    width: 64px; height: 64px; background: var(--accent-red); flex: none;
  }
  .brand-name {
    color: var(--text-light); font-weight: 400; font-size: 50px;
    letter-spacing: 2px; text-transform: uppercase; white-space: nowrap;
  }

  .card-back {
    position: absolute; left: 278px; top: 513px; width: 689px; height: 397px;
    background: var(--card-grey);
  }
  .name-band {
    position: absolute; left: 0; top: 0; width: 100%; height: 140px;
    background: var(--card-white);
  }
  .person-name {
    position: absolute; left: 30px; top: 40px;
    font-size: 29px; font-weight: 700; color: var(--name-grey); letter-spacing: 0.5px;
  }
  .person-role {
    position: absolute; left: 30px; top: 76px;
    font-size: 22px; color: var(--name-grey);
  }
  .contact-list { list-style: none; }
  .contact-item {
    position: absolute; left: 28px; display: flex; align-items: center;
    color: var(--text-light); font-size: 23px;
  }
  .contact-item svg { width: 40px; height: 32px; margin-right: 11px; flex: none; }
  .contact-phone { top: 171px; }
  .contact-email { top: 242px; }
  .contact-web { top: 311px; }
</style>
</head>
<body>
<div class="canvas">
  <section class="card-front">
    <div class="brand">
      <span class="brand-square"></span>
      <span class="brand-name">Framewise Build</span>
    </div>
  </section>

  <section class="card-back">
    <div class="name-band">
      <p class="person-name">MARCUS HELBY</p>
      <p class="person-role">Director</p>
    </div>
    <ul class="contact-list">
      <li class="contact-item contact-phone">
        <svg viewBox="0 0 40 32" aria-hidden="true">
          <rect x="2" y="1" width="16" height="30" rx="2" fill="none" stroke="var(--accent-red)" stroke-width="1.6"/>
          <rect x="5" y="5" width="10" height="18" fill="none" stroke="var(--accent-red)" stroke-width="1.2"/>
          <circle cx="10" cy="27" r="1.5" fill="var(--accent-red)"/>
        </svg>
        0427 593184
      </li>
      <li class="contact-item contact-email">
        <svg viewBox="0 0 40 32" aria-hidden="true">
          <rect x="1" y="8" width="28" height="16" fill="none" stroke="var(--accent-red)" stroke-width="1.6"/>
          <path d="M1 8 L15 18 L29 8 M1 24 L11 15 M29 24 L19 15" fill="none" stroke="var(--accent-red)" stroke-width="1.4"/>
        </svg>
        marcus@framewisebuild.com.au
      </li>
      <li class="contact-item contact-web">
        <svg viewBox="0 0 40 32" aria-hidden="true">
          <text x="0" y="14" font-size="11" fill="var(--accent-red)" font-family="Arimo, Arial, sans-serif">www</text>
          <path d="M26 10 L26 28 L30 24 L33 31 L35 30 L32 23 L37 23 Z" fill="var(--text-light)" stroke="var(--accent-red)" stroke-width="1.2"/>
        </svg>
        www.framewisebuild.com.au
      </li>
    </ul>
  </section>
</div>
</body>
</html>
```